Vertical Banner

I need an eye-catching banner created for street fairs, indoor and outdoor events to draw attention to our language school. It will be to print on this banner (specs included):
https://www.plivorasupply.com/tag/617/Retractable-Banners/product/5173-48/Basic-Rollup-Banner-Stand-29-14

I want the banner to be:
- SIMPLE
- Eye catching (not busy with too many pictures or information)
- It should say at top prominently: "Come learn a language!" and have our name.
- Below these languages should be large and eye-catching: Spanish, Chinese, French, Russian, German, Italian, Farsi, Turkish, Portuguese, ASL, Cantonese, Japanese, Korean, Vietnamese, Arabic, Dutch, more... (if some need to be cut our because of overcrowding let me know OR we can make some big and others small)
- Below this it should have GROUP & PRIVATE LESSONS
- It should be colorful and make people think of things international - perhaps national flags in background? Or images of world famous monuments? Could be image of adutls in a classroom. Sth that gets people excited about travel and language learning
- It should have our contact info VERY large at bottom:
Quill Languages -
San Francisco, Silicon Valley & New York City
www.quilllanguagesf.com
415-962-4051
info@quilllanguagesf.com
(this can be smaller)
Four Halvorsen Plaza
Lobby 3
San Francisco, CA 94127

Hey Designers, please feel free to do a rough take on it. I don't need you to spend too much time, just give me a general idea of how you would make it look, then i know we can go from there later and refine it. Feel free to make it more of a quick sketch to show how you would do it.

Target Market(s)

adults from about 25-55 years old, educated, employed and typically world travellers

Industry/Entity Type

School

Colors
86cfc6
00a990
cadf82
acd036
9bcb3c
fbed22
f78f20
ffc214
f37122

Requirements
Must have
• Must be simple! Too many banners put way too much information and pictures. I want someone to walk by and immediately know we teach foreign languages. Must have bright colors and large font for languages offered
Should not have
• Should not be too full of images and design that distract the viewer from seeing the main thing I want them to see: that we teacher languages

```html
<!DOCTYPE html>
<html lang="en">
<head>
<meta charset="utf-8">
<title>Quill Languages – Rollup Banner</title>
<link rel="stylesheet" href="https://fonts.googleapis.com/css2?family=Oswald:wght@500;600;700&family=Anton&family=Lobster&display=swap">
<style>
  :root {
    --page-bg: #d7dadd;
    --banner-bg: #2b2a2c;
    --brand-green: #0a8a3a;
    --footer-green: #078a3b;
    --headline-yellow: #fbed22;
    --ribbon-yellow: #fff200;
    --ribbon-green: #0b9a3e;
    --text-white: #ffffff;
    --ink-dark: #1f1f1f;
  }
  * { box-sizing: border-box; margin: 0; padding: 0; }
  html, body {
    width: 1200px;
    height: 1175px;
    overflow: hidden;
    background: var(--page-bg);
  }
  .banner {
    position: absolute;
    left: 385px;
    top: 20px;
    width: 430px;
    height: 1135px;
    background: var(--banner-bg);
    display: flex;
    flex-direction: column;
    align-items: center;
    overflow: hidden;
  }
  .brand {
    margin-top: 70px;
    text-align: center;
  }
  .brand-name {
    font-family: "Oswald", sans-serif;
    font-weight: 700;
    font-size: 62px;
    line-height: 1;
    color: var(--brand-green);
    letter-spacing: 0.5px;
  }
  .headline {
    margin-top: 40px;
    font-family: "Anton", sans-serif;
    color: var(--headline-yellow);
    text-align: center;
    text-transform: uppercase;
    line-height: 1;
  }
  .headline-top { display: block; font-size: 64px; letter-spacing: -0.5px; }
  .headline-main { display: block; font-size: 84px; letter-spacing: -0.5px; margin-top: 4px; }
  .language-list {
    margin-top: 28px;
    list-style: none;
    font-family: "Oswald", sans-serif;
    font-weight: 600;
    font-size: 25px;
    color: var(--text-white);
    text-align: center;
    line-height: 45px;
    letter-spacing: -0.3px;
  }
  .lessons-ribbon {
    position: relative;
    margin-top: 22px;
    width: 390px;
    height: 72px;
  }
  .lessons-ribbon svg { position: absolute; inset: 0; }
  .lessons-label {
    position: absolute;
    inset: 0;
    display: flex;
    align-items: center;
    justify-content: center;
    font-family: "Lobster", cursive;
    font-size: 30px;
    color: var(--ink-dark);
    transform: rotate(-2deg);
    padding-bottom: 6px;
  }
  .classroom-photo {
    margin-top: 12px;
    width: 100%;
    height: 250px;
    background: linear-gradient(120deg, #2a2a2a 0%, #3a3a3a 55%, #6b3a45 78%, #c8345a 100%);
  }
  .contact {
    margin-top: auto;
    width: 100%;
    height: 190px;
    background: var(--footer-green);
    font-family: "Oswald", sans-serif;
    font-weight: 600;
    text-align: center;
    padding-top: 22px;
  }
  .contact-cities { color: var(--headline-yellow); font-size: 19px; line-height: 26px; }
  .contact-row {
    color: var(--headline-yellow);
    font-size: 19px;
    line-height: 28px;
    display: flex;
    justify-content: center;
    align-items: center;
    gap: 6px;
  }
  .contact-row .gap { width: 10px; }
  .contact-email { font-weight: 500; font-size: 16px; }
  .contact-icon { width: 15px; height: 15px; }
  .contact-address { color: var(--text-white); font-size: 19px; line-height: 25px; margin-top: 2px; }
</style>
</head>
<body>
  <main class="banner">
    <header class="brand">
      <div class="brand-name">Quill Languages</div>
    </header>

    <h1 class="headline">
      <span class="headline-top">Come learn a</span>
      <span class="headline-main">Language!</span>
    </h1>

    <ul class="language-list">
      <li>Spanish, Chinese, French, Russian,</li>
      <li>German, Italian, Farsi, Turkish,</li>
      <li>Portuguese, ASL, Cantonese,</li>
      <li>Japanese, Korean, Arabic,</li>
      <li>Vietnamese, Dutch, more...</li>
    </ul>

    <div class="lessons-ribbon">
      <svg viewBox="0 0 390 72" width="390" height="72" aria-hidden="true">
        <polygon points="8,14 382,2 374,30 388,56 16,70 24,42" fill="var(--ribbon-green)"/>
        <polygon points="2,16 386,4 374,30 386,52 10,64 20,40" fill="var(--ribbon-yellow)"/>
      </svg>
      <div class="lessons-label">Group &amp; Private Lessons</div>
    </div>

    <div class="classroom-photo" role="img" aria-label="Chalkboard with greetings written in many languages and a smiling student with crossed arms"></div>

    <footer class="contact">
      <div class="contact-cities">San Francisco, Silicon Valley &amp; New York City</div>
      <div class="contact-row">
        <svg class="contact-icon" viewBox="0 0 16 16" aria-hidden="true">
          <circle cx="8" cy="8" r="8" fill="var(--headline-yellow)"/>
          <path d="M5.5 4.2c.4-.3.9-.2 1.1.2l.7 1.3c.2.4.1.8-.2 1l-.5.4c.4.9 1.1 1.7 2 2.1l.4-.5c.3-.3.7-.4 1-.2l1.3.7c.4.2.5.7.2 1.1l-.5.7c-.5.6-1.3.7-2 .4-2-.9-3.5-2.5-4.3-4.5-.3-.7-.1-1.5.5-2z" fill="var(--footer-green)"/>
        </svg>
        <span>415-962-4051</span>
        <span class="gap"></span>
        <svg class="contact-icon" viewBox="0 0 16 16" aria-hidden="true" fill="none" stroke="var(--headline-yellow)" stroke-width="1.3">
          <circle cx="8" cy="8" r="6.5"/>
          <ellipse cx="8" cy="8" rx="3" ry="6.5"/>
          <line x1="1.5" y1="8" x2="14.5" y2="8"/>
        </svg>
        <span>www.quilllanguagesf.com</span>
      </div>
      <div class="contact-row contact-email">
        <svg class="contact-icon" viewBox="0 0 16 16" aria-hidden="true" fill="none" stroke="var(--headline-yellow)" stroke-width="1.3">
          <circle cx="8" cy="8" r="6.8"/>
          <rect x="4.3" y="5.4" width="7.4" height="5.2"/>
          <polyline points="4.3,5.4 8,8.4 11.7,5.4"/>
        </svg>
        <span>info@quilllanguagesf.com</span>
      </div>
      <div class="contact-address">Four Halvorsen Plaza, Lobby 3<br>San Francisco, CA 94127</div>
    </footer>
  </main>
</body>
</html>
```